BrightCareWorks.com, a web based eHealth startup, needs a URL landing page.

We will be building a portfolio of mocked up website screen shots of our products that we will use to engage prospective customers. We would like to start with the company's URL landing page in order to quickly capture a client's interest and identify a graphic artist that we think has the understanding of the feel/UI we are looking for and the talent to meet our expectations. The two solutions we would like to showcase are "BrightCareDialogue" (BCD) and "BrightCareCircle" (BCC).

BCD is a product for improving hospital inpatient communication using tablets and smart phones. Key descriptors for this solution would be, "Improve communication between the patient, the health care team, and the family care team", "Improve communication between Health Team members", and "Monitor for success and improvement opportunities of administrative goals using direct patient feedback."

BCC is a product for improving patient communication after discharge using tablets, smart phones, and computers. Key descriptors for this solution would be, "Transition support to the Family Care Team", "Stay connected after discharge by creating a CareCircle of support", and "Monitor progress, provide encouragement, and coordinate support of loved ones"

The goal of the site will be to give potential customers the impression/feeling of great communication, happiness, and health to patients and staff in the hospital and patients, family, and health care providers outside of the hospital. We are hoping to build a relationship with a talented graphic artist as we continue to grow.
Updates

                                        Hello all, I'm trying to upload a logo file to the project brief, but I'm having a little trouble. I have contacted customer service to request a little help. I will also try and find some examples of pages that may have the look I was thinking of. I didn't try to find anything at the start of the project because I was interested to see if there was a design that I may not have thought of. I can certainly try to find some examples though. As for the logo, I tried to put something together on Photoshop, though I also did one on PowerPoint. All I did for now was use BrightCareWroks where the My was in freestyle script, Health was in Adobe Caslon, the e at the end of Health was in freestyle script again, and the Solutions was in Adobe Caslon again. I also made the freestyle script a bright blue and the Adobe Caslon black in color. This was just what I tried first. Underneath the script I had three circles overlapping so that the point at which they all intersected was in the shape of a shield. This symbol stood for "patient centered care". I guess I'll be posting a project for a logo design soon as well to help refine this. This is my first time using a design site like this so I apologize if there is information needed that I have not provided in a easy to use format. I will certainly extend the deadline if more time is needed.  Thank you and please feel free to send any messages or comments. Thanks again.  

Industry/Entity Type

Building

Requirements
Must have
• A banner with scrolling pictures depicting scenes of patients of all ages happily interacting with hospital health team members, people (patients and nurses/doctors) using tablets, smart phones, and computers in the in the hospital, and patients (elderly and 10-15 years old) using happily using a tablet, smart phone, and/or computer.
• Clean, clutter free look.
• Buttons for [Home], [Solutions], [Platform Model], and [Contact Us].

```html
<!DOCTYPE html>
<html lang="en">
<head>
<meta charset="utf-8">
<title>BrightCareWorks — Home</title>
<link rel="stylesheet" href="https://fonts.googleapis.com/css2?family=Yanone+Kaffeesatz:wght@300;400;700&family=Arimo:wght@400;700&display=swap">
<style>
:root{
  --brand:#1aa3c9;
  --brand-dark:#1589ab;
  --hero-top:#12a6cd;
  --hero-bottom:#86d4ec;
  --text:#555;
  --footer-bg:#b9e4f0;
  --field-bg:#9fd8e8;
  --field-line:#7cc6dc;
  --white:#fff;
}
*{margin:0;padding:0;box-sizing:border-box}
html,body{width:784px;height:1200px;overflow:hidden;background:var(--white)}
body{position:relative;font-family:'Arimo',Arial,sans-serif;color:var(--text)}
.abs{position:absolute}

/* header */
.site-header{left:0;top:0;width:784px;height:70px;background:linear-gradient(#fff,#f1f8fb)}
.brand{left:14px;top:5px;width:88px;display:flex;flex-direction:column;align-items:center;gap:3px}
.brand-dot{width:40px;height:40px;border-radius:50%;background:var(--brand)}
.brand-name{font-family:'Yanone Kaffeesatz',sans-serif;font-weight:400;font-size:14px;line-height:15px;color:var(--brand);white-space:nowrap}
.main-nav a{position:absolute;top:22px;height:48px;line-height:48px;font-family:'Yanone Kaffeesatz',sans-serif;font-weight:300;font-size:23px;color:var(--brand);text-decoration:none;white-space:nowrap}
.main-nav a.is-active{background:var(--brand);color:var(--white);border-radius:4px 4px 0 0;width:83px;text-align:center}

/* hero */
.hero{left:0;top:70px;width:784px;height:376px;background:linear-gradient(var(--hero-top),var(--hero-bottom))}
.hero-photo{left:0;top:0;width:450px;height:376px;background:linear-gradient(135deg,#e8d3b4 0%,#dfe9f2 45%,#cfe0ee 70%,#d9c4a0 100%)}
.hero-title{left:366px;top:102px;font-family:'Yanone Kaffeesatz',sans-serif;font-weight:700;font-size:46px;color:var(--white);line-height:1;white-space:nowrap}
.hero-text{left:367px;top:160px;width:360px;font-family:'Yanone Kaffeesatz',sans-serif;font-weight:300;font-size:31px;line-height:29px;color:var(--white)}
.hero-dots span{position:absolute;top:345px;width:18px;height:18px;border-radius:50%;background:var(--brand)}
.hero-dots span.is-current{background:var(--white)}
.hero-shade{left:0;top:446px;width:784px;height:24px;background:linear-gradient(#eef7fa,#fff)}

/* solutions */
.devices{left:44px;top:524px;width:258px;height:188px;border-radius:10px;background:linear-gradient(160deg,#cdeef7,#8ed3e6)}
.solution h2{font-family:'Yanone Kaffeesatz',sans-serif;font-weight:300;font-size:29px;color:var(--brand);line-height:1;white-space:nowrap}
.solution h2 b{font-weight:700}
.solution p{margin-top:6px;font-size:11px;line-height:13.5px;width:370px}

/* about */
.about h1{font-family:'Yanone Kaffeesatz',sans-serif;font-weight:300;font-size:46px;color:var(--brand);line-height:1}
.about p{margin-top:8px;width:712px;font-size:11.2px;line-height:13.5px}
.btn{display:inline-block;background:var(--brand);color:var(--white);font-family:'Yanone Kaffeesatz',sans-serif;font-weight:700;font-size:17px;border-radius:6px;text-align:center}
.about .btn{margin-top:15px;width:61px;height:28px;line-height:28px}

/* footer */
.site-footer{left:0;top:996px;width:784px;height:204px;background:var(--footer-bg)}
.footer-title{font-family:'Yanone Kaffeesatz',sans-serif;font-weight:700;font-size:19px;color:var(--brand-dark)}
.footer-links{list-style:none;margin-top:9px;margin-left:2px}
.footer-links li{font-size:10.3px;line-height:11.6px;color:var(--brand-dark)}
.field{position:absolute;left:0;width:208px;background:var(--field-bg);border:1px solid var(--field-line);border-radius:4px;font-size:10px;font-weight:700;color:var(--brand-dark);padding:6px 10px}
.submit{position:absolute;left:-3px;width:62px;height:20px;line-height:20px;font-family:'Arimo',Arial,sans-serif;font-size:10px;border-radius:6px}
.contact-lines{margin-top:5px;margin-left:4px;font-size:10px;line-height:11.6px;color:var(--brand-dark)}
.social{display:flex;gap:6px;margin-top:14px;margin-left:2px}
.social span{width:24px;height:24px;border-radius:3px;background:#4f7f92}
</style>
</head>
<body>

<header class="abs site-header">
  <div class="abs brand">
    <span class="brand-dot"></span>
    <span class="brand-name">BrightCareWorks</span>
  </div>
  <nav class="main-nav">
    <a class="is-active" style="left:117px">HOME</a>
    <a style="left:213px">ABOUT US</a>
    <a style="left:317px">SOLUTIONS</a>
    <a style="left:430px">PLATFORM MODEL</a>
    <a style="left:589px">CONTACT US</a>
  </nav>
</header>

<section class="abs hero">
  <div class="abs hero-photo" role="img" aria-label="Photo of a smiling young patient in a hospital bed using a smartphone"></div>
  <h2 class="abs hero-title">Monitor for Success</h2>
  <p class="abs hero-text">Monitor improvement opportunities of administrative goals using direct patient feedback</p>
  <div class="hero-dots">
    <span style="left:681px"></span>
    <span class="is-current" style="left:713px"></span>
    <span style="left:744px"></span>
  </div>
</section>
<div class="abs hero-shade"></div>

<div class="abs devices" role="img" aria-label="Tablet and smartphone showing the BrightCareDialogue and BrightCareCircle apps"></div>

<section class="abs solution" style="left:406px;top:516px">
  <h2><b>BCD</b> ‘BrightCareDialogue’</h2>
  <p>BCD offers Improve communication between the patient, the health care team, and the family care team", "Improve communication between Health Team members", and "Monitor for success and improvement opportunities of administrative goals using direct patient feedback.</p>
</section>
<section class="abs solution" style="left:406px;top:628px">
  <h2><b>BCC</b> ‘BrightCareCircle’</h2>
  <p>Transition support to the Family Care Team", "Stay connected after discharge by creating a CareCircle of support", and "Monitor progress, provide encouragement, and coordinate support of loved ones</p>
</section>

<section class="abs about" style="left:45px;top:782px">
  <h1>ABOUT US</h1>
  <p>Lorem ipsum dolor sit amet, consectetur adipisicing elit, sed do eiusmod tempor incididunt ut labore et dolore magna aliqua. Ut enim ad minim veniam, quis nostrud exercitation ullamco laboris nisi ut aliquip ex ea commodo consequat. Lorem ipsum dolor sit amet, consectetur adipisicing elit, sed do eiusmod tempor incididunt ut labore et dolore magna aliqua. Ut enim ad minim veniam, quis nostrud exercitation ullamco laboris nisi ut aliquip ex ea commodo consequat.</p>
  <a class="btn">more</a>
</section>

<footer class="abs site-footer">
  <div class="abs" style="left:24px;top:29px">
    <div class="footer-title">NAVIGATION</div>
    <ul class="footer-links">
      <li>HOME</li><li>ABOUT US</li><li>SOLUTIONS</li><li>PLATFORM MODEL</li><li>CONTACT US</li>
    </ul>
  </div>
  <div class="abs" style="left:246px;top:29px;width:210px;height:160px">
    <div class="footer-title">EMAIL US</div>
    <div class="field" style="top:25px;height:23px">email</div>
    <div class="field" style="top:52px;height:23px">subject</div>
    <div class="field" style="top:78px;height:55px">content</div>
    <a class="btn submit" style="top:139px">submit</a>
  </div>
  <div class="abs" style="left:559px;top:29px">
    <div class="footer-title">CONTACT US</div>
    <div class="contact-lines">
      12 Harbour Lane Fenwick City,<br>London, EC482, UK<br>Tel: +12 55501234<br>Fax: +12 55501234<br>Mail: info@BrightCareWorks.com
    </div>
    <div class="social"><span></span><span></span><span></span><span></span><span></span></div>
  </div>
</footer>

</body>
</html>
```